Website design for management consulting firm

We need a web design for a new consulting company based in Boston, MA called "Quillmoor Ridge Consulting." This webpage will be simple home page, with a "contact us" page, that describes the services of the consulting firm. The company provides strategic planning, business assessment, process re-designs, and other management consulting functions. I would like the website to look high-tech. A logo was already created via Artsy Hive.

Target Market(s)

Other business owners across a wide spectrum of industries - from IT to retail.

Industry/Entity Type

It Company

Number of Pages Required

3 page

Colors
0455a3
ffffff

Requirements
Must have
• Front page that provides generic text / overview of the firm. A "services" tab that describes consulting services. A "contact us" tab that provides either a form to contact us or just the contact email address of the company. info@quillmoorridgeconsulting.example

```html
<!DOCTYPE html>
<html lang="en">
<head>
<meta charset="utf-8">
<title>Contact Us – Quillmoor Ridge Consulting</title>
<link href="https://fonts.googleapis.com/css2?family=Open+Sans:wght@300;400;600;700&display=swap" rel="stylesheet">
<style>
:root{
  --brand:#0455a3;
  --brand-mid:#3a78b8;
  --brand-light:#6a9bcb;
  --white:#ffffff;
  --ink:#333333;
  --muted:#9a9a9a;
  --line:#d6d6d6;
  --submit:#9b9b9b;
  --footer-bg:#f7f7f7;
  --bar:#414141;
}
*{margin:0;padding:0;box-sizing:border-box}
html,body{width:899px;height:1200px;overflow:hidden;background:var(--white)}
body{position:relative;font-family:'Open Sans',sans-serif;color:var(--ink)}
.abs{position:absolute}

/* header */
.site-header{position:absolute;left:0;top:0;width:899px;height:70px;background:var(--white)}
.brand{position:absolute;left:121px;top:20px;display:flex;align-items:center;gap:7px}
.brand-mark{width:24px;height:24px;background:var(--brand)}
.brand-name{font-size:14px;font-weight:700;color:#1d1d1d;line-height:1}
.main-nav a{position:absolute;top:0;height:70px;line-height:94px;font-size:12px;color:var(--brand);text-decoration:none}
.main-nav a.active{background:var(--brand);color:var(--white);width:91px;text-align:center}

/* hero */
.hero{position:absolute;left:0;top:70px;width:899px;height:180px;
  background:linear-gradient(90deg,#a8b3bf 0%,#7d8ea0 40%,#3e5570 70%,#1f344d 100%)}
.hero-title{position:absolute;left:118px;top:64px;font-size:26px;font-weight:400;color:var(--white);letter-spacing:.5px}
.hero-rule{position:absolute;left:120px;top:98px;width:200px;height:1px;background:var(--white)}
.hero-frame{position:absolute;left:175px;top:98px;width:246px;height:46px;border-left:1px solid var(--white);border-bottom:1px solid var(--white)}
.hero-kicker{position:absolute;left:190px;top:105px;font-size:13px;font-weight:300;color:var(--white)}
.hero-lead{position:absolute;left:190px;top:121px;font-size:16px;font-weight:700;color:var(--white)}

/* form */
.form-area{position:absolute;left:0;top:250px;width:899px;height:270px;
  background:radial-gradient(ellipse at 50% 40%,#f1f1f1 0%,#fafafa 45%,#ffffff 75%)}
.form-title{position:absolute;left:0;top:280px;width:899px;text-align:center;font-size:20px;font-weight:600;color:var(--brand)}
.field{position:absolute;border:1px solid var(--line);background:var(--white);font-size:8px;color:var(--muted);padding:7px 7px}
.submit{position:absolute;left:206px;top:458px;width:487px;height:29px;background:var(--submit);color:var(--white);font-size:11px;text-align:center;line-height:29px}

/* contact tiles */
.tile{position:absolute;top:520px;width:185px;height:151px;color:var(--white);text-align:center;font-size:9.5px;line-height:16px}
.tile svg{display:block;margin:36px auto 18px}
.tile-phone{left:175px;background:var(--brand)}
.tile-place{left:360px;background:var(--brand-mid)}
.tile-mail{left:545px;background:var(--brand-light)}

.map{position:absolute;left:0;top:671px;width:899px;height:305px;background:linear-gradient(160deg,#cbc7c1 0%,#bfbab3 55%,#aeb79a 100%)}

/* footer */
.site-footer{position:absolute;left:0;top:976px;width:899px;height:179px;background:var(--footer-bg)}
.foot-brand{position:absolute;left:127px;top:1011px;display:flex;align-items:center;gap:6px}
.foot-brand .brand-mark{width:18px;height:18px}
.foot-brand .brand-name{font-size:11px}
.foot-rule{position:absolute;left:121px;top:1051px;width:169px;height:1px;background:#bdbdbd}
.foot-heading{position:absolute;font-size:12px;font-weight:600;color:var(--brand);letter-spacing:.3px}
.foot-heading.plain{font-weight:400}
.foot-text{position:absolute;font-size:9px;color:var(--ink)}
.foot-list{position:absolute;list-style:none;font-size:9px;line-height:17px;color:var(--ink)}
.news-input{position:absolute;left:127px;top:1111px;width:133px;height:22px;border:1px solid var(--line);background:var(--white)}
.news-go{position:absolute;left:260px;top:1111px;width:30px;height:22px;background:var(--brand);color:var(--white);font-size:11px;text-align:center;line-height:22px}
.social{position:absolute;left:665px;list-style:none;font-size:9.5px;color:var(--ink)}
.social li{display:flex;align-items:center;gap:10px;height:21px}
.social span.sq{width:19px;height:19px;background:var(--brand)}
.copy-bar{position:absolute;left:0;top:1155px;width:899px;height:45px;background:var(--bar);color:var(--white);font-size:9.5px;text-align:center;line-height:45px}
</style>
</head>
<body>

<header class="site-header">
  <div class="brand"><span class="brand-mark"></span><span class="brand-name">Quillmoor Ridge Consulting</span></div>
  <nav class="main-nav">
    <a style="left:372px">HOME</a>
    <a style="left:434px">ABOUT</a>
    <a style="left:500px">BLOG</a>
    <a style="left:559px">NEWS</a>
    <a style="left:618px">SERVICES</a>
    <a class="active" style="left:687px">CONTACT US</a>
  </nav>
</header>

<section class="hero" role="img" aria-label="Photo of two businessmen reviewing work together">
  <h1 class="hero-title">CONTACT US</h1>
  <div class="hero-rule"></div>
  <div class="hero-frame"></div>
  <p class="hero-kicker">Get in touch with us</p>
  <p class="hero-lead">We are ready to guide you</p>
</section>

<section class="form-area" role="img" aria-label="Faint world map backdrop"></section>
<h2 class="form-title">CONTACT FORM</h2>
<div class="field" style="left:206px;top:323px;width:241px;height:22px">Firstname</div>
<div class="field" style="left:451px;top:323px;width:242px;height:22px">Lastname</div>
<div class="field" style="left:206px;top:349px;width:241px;height:22px">E-mail</div>
<div class="field" style="left:451px;top:349px;width:242px;height:22px">Phone</div>
<div class="field" style="left:206px;top:374px;width:487px;height:81px;font-size:9px">Comments</div>
<div class="submit">Submit</div>

<div class="tile tile-phone">
  <svg width="14" height="24" viewBox="0 0 14 24"><rect x="1" y="1" width="12" height="22" rx="2" fill="none" stroke="#fff" stroke-width="1.6"/><line x1="1" y1="4.5" x2="13" y2="4.5" stroke="#fff" stroke-width="1.2"/><line x1="1" y1="18.5" x2="13" y2="18.5" stroke="#fff" stroke-width="1.2"/><circle cx="7" cy="21" r="1" fill="#fff"/></svg>
  PERSONAL : +01 555 018 2247<br>OFFICE : 0555 310 42 86
</div>
<div class="tile tile-place">
  <svg width="18" height="26" viewBox="0 0 18 26"><path d="M9 1C4.6 1 1 4.5 1 9c0 6 8 16 8 16s8-10 8-16c0-4.5-3.6-8-8-8z" fill="#fff"/><circle cx="9" cy="9" r="3" fill="#3a78b8"/></svg>
  Quillmoor Ridge Consulting<br>text of the printing and<br>typesetting industry.
</div>
<div class="tile tile-mail">
  <svg width="22" height="16" viewBox="0 0 22 16"><rect x="1" y="1" width="20" height="14" fill="none" stroke="#fff" stroke-width="1.5"/><path d="M1 1l10 8 10-8M1 15l7-6M21 15l-7-6" fill="none" stroke="#fff" stroke-width="1.3"/></svg>
  info@quillmoorridgeconsulting.example<br>quillmoorridgeconsulting.example
</div>

<section class="map" role="img" aria-label="Street map showing the office location"></section>

<footer class="site-footer"></footer>
<div class="foot-brand"><span class="brand-mark"></span><span class="brand-name">Quillmoor Ridge Consulting</span></div>
<div class="foot-rule"></div>
<h3 class="foot-heading plain" style="left:127px;top:1067px">NEWSLETTER</h3>
<p class="foot-text" style="left:129px;top:1093px">Sign up Your Newsletter</p>
<div class="news-input"></div>
<div class="news-go">GO</div>

<h3 class="foot-heading" style="left:329px;top:1008px">QUICK LINKS</h3>
<ul class="foot-list" style="left:332px;top:1034px">
  <li>HOME</li><li>About</li><li>Blog</li><li>News</li><li>Services</li><li>Contact us</li>
</ul>

<h3 class="foot-heading" style="left:435px;top:1008px">CONTACT DETAILS</h3>
<ul class="foot-list" style="left:437px;top:1036px">
  <li>Quillmoor Ridge Consulting</li>
  <li>#14, Larkfield Row, Harbor Quarter</li>
  <li>Boston, Massachusetts, USA</li>
  <li>Phone : +01 555 0193 774</li>
  <li>Email : info@quillmoorridgeconsulting.example</li>
</ul>

<h3 class="foot-heading" style="left:659px;top:1008px">FOLLW US ON</h3>
<ul class="social" style="top:1036px">
  <li><span class="sq"></span>newsfeed</li>
  <li><span class="sq"></span>shortposts</li>
  <li><span class="sq"></span>videocast</li>
  <li><span class="sq"></span>circles</li>
</ul>

<div class="copy-bar">© 2015 Quillmoor Ridge Consulting. allright Reserved</div>

</body>
</html>
```